Mobile Recording Studio needs business cards

Open to seeing a creative design, but I want to emphasis my logo and minimize the name/title and company information. Possible a fully black background on card.

My company is a mobile sound recording studio. ok to include a my trailer (actual or cartoon) on the card. My initial thought is more straight forward, but a good design will win me over.

SPECS:
CMYK color mode
High (300ppi) raster effect.
cover bleed area
please deliver: Illustrator file with layers and a pdf at completion.

Name and info for the business card:

Dallin Perry
ADR Mixer

email: Dallin@MixVault.com

address:
248 - 5170 East Hollister
Vancouver, BC V5R 2J4

phone:
604.518.2093 office

website:
www.MixVault.com

FB: @MixVault

Instagram: @TheMixVault

Industry/Entity Type

Television Production

Contact Information for Business Card

Dallin Perry
ADR Mixer

email: Dallin@MixVault.com

address:
248 - 5170 East Hollister
Vancouver, BC V5R 2J4

phone:
604.518.2093 office

website:
www.MixVault.com

FB: @MixVault

Instagram: @TheMixVault

Colors

Designer to choose colors to be used in the design.

Requirements
Must have
• emphasis my logo and minimize the name/title and company information.
• SPECS:
• CMYK color mode
• High (300ppi) raster effect.
• cover bleed area
• please deliver: Illustrator file with layers and a pdf at completion.
Nice to have
• maybe include the following:
• all black background or black theme
• my work trailer (actual or cartoon) refer to Instagram: @TheMixVault

```html
<!DOCTYPE html>
<html lang="en">
<head>
<meta charset="utf-8">
<title>MixVault Business Card</title>
<link rel="stylesheet" href="https://fonts.googleapis.com/css2?family=Archivo:wght@400;500;700&display=swap">
<style>
  :root {
    --backdrop: #6a6b6d;
    --card: #000000;
    --ink: #ffffff;
    --silver: #cfcfd1;
    --shadow: rgba(0, 0, 0, 0.35);
  }
  * { margin: 0; padding: 0; box-sizing: border-box; }
  html, body {
    width: 1200px;
    height: 1200px;
    overflow: hidden;
    background: var(--backdrop);
    font-family: "Archivo", Arial, sans-serif;
  }
  .card {
    position: absolute;
    left: 252px;
    width: 704px;
    height: 402px;
    background: var(--card);
    box-shadow: 10px 10px 14px var(--shadow);
    color: var(--ink);
  }
  .card--front { top: 148px; }
  .card--back { top: 656px; }

  .brand {
    position: absolute;
    inset: 0;
    display: flex;
    align-items: center;
    justify-content: center;
  }
  .brand__name {
    font-size: 84px;
    font-weight: 700;
    color: var(--silver);
    letter-spacing: -1px;
  }

  .person {
    position: absolute;
    left: 46px;
    top: 44px;
  }
  .person__name {
    font-size: 24px;
    font-weight: 700;
    letter-spacing: 0.6px;
    text-transform: uppercase;
    line-height: 1;
  }
  .person__title {
    margin-top: 10px;
    font-size: 16px;
    font-weight: 500;
    line-height: 1;
  }

  .contact {
    position: absolute;
    left: 464px;
    top: 240px;
    list-style: none;
  }
  .contact__item {
    display: flex;
    align-items: flex-start;
    gap: 8px;
    font-size: 12px;
    font-weight: 500;
    letter-spacing: 0.5px;
    line-height: 17px;
    margin-bottom: 11px;
  }
  .contact__icon {
    width: 17px;
    height: 17px;
    flex: none;
    fill: none;
    stroke: var(--ink);
    stroke-width: 1.1;
    stroke-linecap: round;
    stroke-linejoin: round;
  }
</style>
</head>
<body>
  <section class="card card--front">
    <div class="brand">
      <span class="brand__name">MixVault</span>
    </div>
  </section>

  <section class="card card--back">
    <div class="person">
      <p class="person__name">Dallin Perry</p>
      <p class="person__title">ADR Mixer</p>
    </div>

    <ul class="contact">
      <li class="contact__item">
        <svg class="contact__icon" viewBox="0 0 18 18" aria-hidden="true">
          <circle cx="9" cy="9" r="7.5"/>
          <circle cx="9" cy="9" r="2.6"/>
          <path d="M11.6 6.6v3.4c0 1.4 2.4 1.4 2.4-0.6"/>
        </svg>
        <span>Dallin@MixVault.com</span>
      </li>
      <li class="contact__item">
        <svg class="contact__icon" viewBox="0 0 18 18" aria-hidden="true">
          <circle cx="9" cy="9" r="7.5"/>
          <ellipse cx="9" cy="9" rx="3.2" ry="7.5"/>
          <path d="M1.5 9h15M2.6 5.2h12.8M2.6 12.8h12.8"/>
        </svg>
        <span>www.MixVault.com</span>
      </li>
      <li class="contact__item">
        <svg class="contact__icon" viewBox="0 0 18 18" aria-hidden="true">
          <path d="M3.2 1.8l2.6-0.4 1.6 3.6-1.8 1.4c0.9 2.3 2.7 4.2 5 5.2l1.4-1.8 3.6 1.6-0.4 2.6c-0.2 1-1.1 1.6-2.1 1.5C7 14.8 2.9 10.7 2 4c-0.1-1 0.4-1.9 1.2-2.2z"/>
        </svg>
        <span>604.518.2093</span>
      </li>
      <li class="contact__item">
        <svg class="contact__icon" viewBox="0 0 18 18" aria-hidden="true">
          <path d="M9 17s-5.5-6-5.5-10a5.5 5.5 0 0 1 11 0c0 4-5.5 10-5.5 10z"/>
          <circle cx="9" cy="7" r="2"/>
        </svg>
        <span>248 - 5170 East Hollister<br>Vancouver, BC V5R 2J4</span>
      </li>
    </ul>
  </section>
</body>
</html>
```